Rural photograpy business card design

I need a business card for my photography business, brianna delys photography. I would like my logo and pre designed font used on the card. Also my business specialises in photographing rural australia (e.g. shearing sheds, livestock, landscapes, farms), so a rural or country feel to the card would be great. I would like to keep the colours fresh but not too overpowering or juvenile.
Updates

Hi,

Could you please add my facebook page to the card - www.snapfolio-example.com/Brianna/Delys/Photography.
Thanks,
Brianna.

Reason: I have uploaded two photos I would like either one used on the card.

Target Market(s)

Farmers, country people from their mid twenties onwards

Industry/Entity Type

Business

Contact Information for Business Card

Brianna Delys Photography. Brianna Pemberton. 5182 Yarrowby-Tullagong Road, Meandarra Qld 4422. 0471602394.

Requirements
Must have
• My pre-designed logo and font. Also please add my facebook address - www.snapfolio-example.com/BriannaDelys/Photography.
Please use one of the photos I have provided.
Should not have
• Peoples faces on the card.

```html
<!DOCTYPE html>
<html lang="en">
<head>
<meta charset="utf-8">
<title>Brianna Delys Photography – Business Card</title>
<link rel="stylesheet" href="https://fonts.googleapis.com/css2?family=Questrial&family=Mulish:wght@700&display=swap">
<style>
  :root {
    --backdrop: #e9dccb;
    --card-tan: #c8a174;
    --card-tan-deep: #b48c5f;
    --band-cream: #f1e8df;
    --ink: #1c1610;
    --paper: #ffffff;
    --sky-top: #b9925f;
    --sky-glow: #e3a24e;
    --flock-dark: #2e2219;
  }
  html, body {
    margin: 0;
    padding: 0;
    width: 1200px;
    height: 1000px;
    overflow: hidden;
    background: var(--backdrop);
    font-family: "Questrial", "Century Gothic", sans-serif;
  }
  .canvas {
    position: relative;
    width: 1200px;
    height: 1000px;
  }
  .card {
    position: absolute;
    overflow: hidden;
    box-shadow: 0 10px 24px rgba(60, 40, 20, 0.35);
  }

  /* Front card */
  .card-front {
    left: 170px;
    top: 30px;
    width: 790px;
    height: 450px;
    background: var(--card-tan);
  }
  .front-field {
    position: absolute;
    left: 0;
    bottom: 0;
    width: 100%;
    height: 150px;
    background: linear-gradient(180deg, var(--card-tan) 0%, var(--card-tan-deep) 100%);
  }
  .brand-mark {
    position: absolute;
    display: flex;
    flex-direction: column;
    align-items: center;
    color: var(--paper);
    font-size: 21px;
    letter-spacing: 1px;
    line-height: 1.15;
    text-align: center;
  }
  .brand-mark .dot {
    width: 46px;
    height: 46px;
    border: 3px solid currentColor;
    border-radius: 50%;
    margin-bottom: 8px;
  }
  .card-front .brand-mark {
    left: 48px;
    top: 28px;
  }
  .name-band {
    position: absolute;
    left: 0;
    top: 145px;
    width: 100%;
    height: 155px;
    background: var(--band-cream);
    display: flex;
    flex-direction: column;
    justify-content: center;
    align-items: center;
    padding-left: 90px;
    box-sizing: border-box;
  }
  .person-name {
    font-family: "Mulish", "Century Gothic", sans-serif;
    font-weight: 700;
    font-size: 31px;
    letter-spacing: 1.5px;
    color: var(--ink);
  }
  .person-role {
    font-size: 22px;
    letter-spacing: 5px;
    color: var(--ink);
    margin-top: 2px;
  }
  .contact {
    position: absolute;
    display: flex;
    align-items: flex-start;
    gap: 14px;
    color: var(--paper);
    font-family: "Mulish", "Century Gothic", sans-serif;
    font-weight: 700;
    font-size: 15px;
    letter-spacing: 1px;
    line-height: 1.4;
  }
  .contact svg { flex: none; }
  .contact-phone { left: 42px; top: 330px; }
  .contact-web { left: 42px; top: 380px; }
  .contact-address { left: 540px; top: 345px; }
  .web-square {
    flex: none;
    width: 22px;
    height: 22px;
    background: var(--flock-dark);
    opacity: 0.75;
    margin-top: 3px;
  }

  /* Back card */
  .card-back {
    left: 200px;
    top: 515px;
    width: 800px;
    height: 455px;
  }
  .back-photo {
    position: absolute;
    inset: 0;
    background:
      radial-gradient(circle at 82% 72%, rgba(255, 190, 90, 0.75) 0%, rgba(255, 170, 70, 0) 22%),
      linear-gradient(180deg, var(--sky-top) 0%, var(--sky-glow) 45%, #6b4a2c 62%, var(--flock-dark) 100%);
  }
  .logo-band {
    position: absolute;
    left: 0;
    top: 95px;
    width: 100%;
    height: 200px;
    background: rgba(255, 255, 255, 0.86);
    display: flex;
    justify-content: center;
    align-items: center;
  }
  .card-back .brand-mark {
    position: static;
    color: var(--ink);
    font-size: 26px;
  }
</style>
</head>
<body>
<main class="canvas">

  <section class="card card-front" aria-label="Business card front">
    <div class="front-field" role="img" aria-label="Faded photo of a flock of sheep in a yard with a gum tree"></div>

    <div class="brand-mark">
      <span class="dot"></span>
      <span>BRIANNA DELYS</span>
      <span>Photography</span>
    </div>

    <div class="name-band">
      <div class="person-name">Brianna Pemberton</div>
      <div class="person-role">Photographer</div>
    </div>

    <div class="contact contact-phone">
      <svg width="22" height="26" viewBox="0 0 22 26" aria-hidden="true">
        <path d="M5 1 L9 1 L10 7 L7 9 Q9 15 13 18 L16 15 L21 17 L21 22 Q19 25 15 24 Q3 19 1 6 Q1 2 5 1 Z" fill="#3a2a1e" opacity="0.75"/>
      </svg>
      <span>+6047-160-2394</span>
    </div>

    <div class="contact contact-web">
      <span class="web-square"></span>
      <span>snapfolio-example.com/Brianna/<br>Delys/Photography</span>
    </div>

    <div class="contact contact-address">
      <svg width="20" height="30" viewBox="0 0 20 30" aria-hidden="true">
        <path d="M10 1 Q19 1 19 10 Q19 17 10 29 Q1 17 1 10 Q1 1 10 1 Z" fill="#3a2a1e" opacity="0.75"/>
        <circle cx="10" cy="10" r="3.5" fill="#c8a174"/>
      </svg>
      <span>5182 Yarrowby-<br>Tullagong Road,<br>Tullagong Vic,<br>3799</span>
    </div>
  </section>

  <section class="card card-back" aria-label="Business card back">
    <div class="back-photo" role="img" aria-label="Photo of a mob of sheep in a yard at sunset with a lone gum tree on the horizon"></div>
    <div class="logo-band">
      <div class="brand-mark">
        <span class="dot"></span>
        <span>BRIANNA DELYS</span>
        <span>Photography</span>
      </div>
    </div>
  </section>

</main>
</body>
</html>
```